Bellmoor Health Standing Banner

Design a standing banner for a community health care clinic. Our website is www.bellmoorhealth.org. On there you can find our list of services. I have uploaded our logo, mission/vision/about us statements, as well as our business cards for contact information and so you have an idea of the theme we are going for.
Our tagline is building a healthier society.

We want the banner to showcase our name, tagline, services, and the contact methods listed on the business card except for the address.

```html
<!DOCTYPE html>
<html lang="en">
<head>
<meta charset="utf-8">
<title>Bellmoor Health Standing Banner</title>
<link href="https://fonts.googleapis.com/css2?family=Lato:ital,wght@0,300;0,400;0,700;0,900;1,400&family=EB+Garamond:ital@1&display=swap" rel="stylesheet">
<style>
  :root {
    --green: #62b040;
    --green-dark: #4f9a32;
    --white: #ffffff;
    --ink: #2b2b2b;
    --page: #e4e4e4;
    --photo-a: #b9b6b1;
    --photo-b: #e9e7e4;
  }
  * { margin: 0; padding: 0; box-sizing: border-box; }
  html, body { width: 1200px; height: 1044px; overflow: hidden; background: var(--page); }
  .canvas { position: relative; width: 1200px; height: 1044px; }
  .banner {
    position: absolute; left: 394px; top: 24px; width: 412px; height: 996px;
    background: var(--green); overflow: hidden;
    font-family: "Lato", sans-serif;
  }
  .hero-photo {
    position: absolute; left: 0; top: 0; width: 412px; height: 400px;
    background: linear-gradient(135deg, var(--photo-b) 0%, var(--photo-a) 45%, #9d9a95 70%, var(--photo-b) 100%);
  }
  .hero-curve { position: absolute; left: 0; top: 290px; width: 412px; height: 120px; }
  .brand-box {
    position: absolute; left: 265px; top: 140px; width: 147px; height: 103px;
    background: rgba(255,255,255,0.82);
    display: flex; flex-direction: column; align-items: center; justify-content: flex-end;
    padding-bottom: 10px;
  }
  .brand-dot { width: 52px; height: 52px; border-radius: 50%; background: var(--green); margin-bottom: 10px; }
  .brand-name { color: var(--green); font-size: 19px; font-weight: 400; letter-spacing: 0.2px; }
  .tagline {
    position: absolute; right: 20px; top: 245px;
    font-family: "EB Garamond", serif; font-style: italic; font-size: 19px; color: var(--white);
  }
  .headline { position: absolute; left: 31px; top: 408px; color: var(--white); }
  .headline-lead { display: block; font-size: 28px; font-weight: 300; line-height: 1.1; }
  .headline-main { display: block; font-size: 37px; font-weight: 900; letter-spacing: -0.6px; line-height: 1.1; }
  .services { position: absolute; left: 0; top: 531px; width: 412px; }
  .service-row { display: grid; grid-template-columns: 136px 136px 136px; column-gap: 2px; margin-bottom: 8px; }
  .service-photo { height: 137px; }
  .service-label { color: var(--white); font-size: 15px; text-align: center; height: 44px; line-height: 40px; }
  .tone-blue { background: linear-gradient(160deg, #eef1f6, #b9c3d6); }
  .tone-grey { background: linear-gradient(160deg, #f1f1f3, #9a9894); }
  .tone-violet { background: linear-gradient(160deg, #eceef6, #a9acc9); }
  .tone-mint { background: linear-gradient(160deg, #cfe6dc, #7fb0c8); }
  .tone-lab { background: linear-gradient(160deg, #f2f2f2, #b4a7b5); }
  .tone-food { background: linear-gradient(160deg, #f3f1ec, #d9663f 60%, #8cc055); }
  .footer-curve { position: absolute; left: 0; top: 880px; width: 412px; height: 116px; }
  .contact { position: absolute; right: 16px; top: 958px; text-align: right; }
  .contact-line { font-size: 13px; color: var(--ink); display: flex; gap: 12px; justify-content: flex-end; align-items: center; }
  .contact-item { display: inline-flex; align-items: center; gap: 5px; }
  .contact-item svg { width: 13px; height: 11px; }
  .web { margin-top: 4px; font-size: 12px; color: var(--green); letter-spacing: 4.2px; font-weight: 700; }
</style>
</head>
<body>
<div class="canvas">
  <section class="banner">
    <div class="hero-photo" role="img" aria-label="Laboratory worker in gloves pouring liquid into a beaker at a bench with bottles and an open notebook"></div>
    <svg class="hero-curve" viewBox="0 0 412 120" aria-hidden="true">
      <path d="M0 90 Q210 125 412 20 L412 120 L0 120 Z" fill="var(--green)"/>
      <path d="M0 84 Q210 118 412 14" fill="none" stroke="var(--white)" stroke-width="5"/>
      <path d="M0 81 Q210 114 412 10" fill="none" stroke="var(--green)" stroke-width="2.5"/>
    </svg>
    <div class="brand-box">
      <span class="brand-dot"></span>
      <span class="brand-name">Bellmoor Health</span>
    </div>
    <p class="tagline">A higher quality of life!</p>

    <h1 class="headline">
      <span class="headline-lead">BUILDING A</span>
      <span class="headline-main">HEALTHIER SOCIETY</span>
    </h1>

    <div class="services">
      <div class="service-row">
        <div>
          <div class="service-photo tone-blue" role="img" aria-label="Doctor measuring blood pressure"></div>
          <p class="service-label">Health Fairs</p>
        </div>
        <div>
          <div class="service-photo tone-grey" role="img" aria-label="Clinic counter with jar of swabs"></div>
          <p class="service-label">Community Clinic</p>
        </div>
        <div>
          <div class="service-photo tone-violet" role="img" aria-label="Syringe and vial on a table"></div>
          <p class="service-label">Substance Abuse</p>
        </div>
      </div>
      <div class="service-row">
        <div>
          <div class="service-photo tone-mint" role="img" aria-label="Gloved hands drawing blood from an arm"></div>
          <p class="service-label">Lab</p>
        </div>
        <div>
          <div class="service-photo tone-lab" role="img" aria-label="Researcher writing beside racks of test tubes"></div>
          <p class="service-label">Clinical Research</p>
        </div>
        <div>
          <div class="service-photo tone-food" role="img" aria-label="Fresh tomatoes and lettuce being prepared"></div>
          <p class="service-label">Nutrition</p>
        </div>
      </div>
    </div>

    <svg class="footer-curve" viewBox="0 0 412 116" aria-hidden="true">
      <path d="M0 116 L0 100 Q205 20 412 75 L412 116 Z" fill="var(--white)"/>
      <path d="M0 96 Q205 14 412 70" fill="none" stroke="var(--green)" stroke-width="3"/>
    </svg>

    <div class="contact">
      <p class="contact-line">
        <span class="contact-item">
          <svg viewBox="0 0 13 11" aria-hidden="true"><path d="M1 4 Q6.5 -1 12 4 L10 5 L9 3.5 L4 3.5 L3 5 Z M3 6 L10 6 L11.5 10.5 L1.5 10.5 Z" fill="var(--green)"/></svg>
          555-014-2290
        </span>
        <span class="contact-item">
          <svg viewBox="0 0 13 11" aria-hidden="true"><rect x="0.5" y="1" width="12" height="9" fill="var(--green)"/><path d="M0.5 1 L6.5 6 L12.5 1 M0.5 10 L5 5 M12.5 10 L8 5" fill="none" stroke="var(--white)" stroke-width="1"/></svg>
          info@bellmoorhealth.org
        </span>
      </p>
      <p class="web">www.bellmoorhealth.org</p>
    </div>
  </section>
</div>
</body>
</html>
```